Personal Motivational Quote Poster Design

I would like to create a poster with some of my favorite quotes to hang in my office. I did similar projects in 2012 and 2014. I've uploaded the winning designs so you can get a better idea of what I'm looking for. I will provide feedback on your design within 24 hours of receiving it.

The poster must contain the following quotes:

“What the pupil must learn, if he learns anything at all, is that the world will do most of the work for you, provided you cooperate with it by identifying how it really works and aligning with those realities. If we do not let the world teach us, it teaches us a lesson.” - Harold Wexbury

“I tackle every big new problem by asking two questions: Who has dealt with this problem well? And what can we learn from them?” - Tom Harlow

“If we can really understand the problem, the answer will come out of it, because the answer is not separate from the problem.” - Ravindra Pallathuri

“Success is nothing more than a few simple disciplines, practiced every day; while failure is simply a few errors in judgment, repeated every day. It is the accumulative weight of our disciplines and our judgments that leads us to either fortune or failure.” - Ned Pilsk

“Inaction breeds doubt and fear. Action breeds confidence and courage.” - Walt Brimsley

“What’s the one thing you can do, such that by doing it, everything else will be easier or unnecessary?” - Lenny Druse

Requirements
Must have
• The poster will be 24" high x 36" long and printed on canvas, so the image you create needs to have a resolution of at least 2700 x 3900.
Nice to have
• I don't have an exact vision for how the poster should look, so I am totally open to you using your creativity to develop, arrange and present the content as you'd like.

That said, I would like an image (photo or posterized image) of the person being quoted along with each quote. I do not have specific images that I would like you to use, so you will need to find the images on your own.

The images don't need to be perfect... I am more interested in the poster relating the essence of the quotes and the people being quoted than I am in perfect photographic images of the people being quoted.

```html
<!DOCTYPE html>
<html lang="en">
<head>
<meta charset="utf-8">
<title>Favorite Quotes Poster</title>
<link href="https://fonts.googleapis.com/css2?family=Montserrat:ital,wght@0,400;1,400&display=swap" rel="stylesheet">
<style>
  :root {
    --bg: #a6efe2;
    --ink: #111111;
    --author: #555555;
    --line: #111111;
    --bar: #ffffff;
    --pink: #fdd3da;
    --purple: #948de6;
    --gray: #e7e7e7;
    --blue: #86d7fd;
    --green: #b2f0a2;
    --yellow: #fdfad3;
    --photo-a: #8a8a8a;
    --photo-b: #3a3a3a;
  }
  * { box-sizing: border-box; margin: 0; padding: 0; }
  html, body { width: 800px; height: 1200px; overflow: hidden; }
  body {
    background: var(--bg);
    font-family: "Montserrat", sans-serif;
    color: var(--ink);
    position: relative;
  }
  .row { position: absolute; left: 31px; width: 738px; height: 193px; }
  .window {
    position: absolute; top: 0; width: 205px; height: 193px;
    border: 1.5px solid var(--line); background: var(--bar);
  }
  .titlebar {
    height: 13px; border-bottom: 1.5px solid var(--line);
    display: flex; justify-content: flex-end; align-items: center; gap: 6px; padding-right: 6px;
  }
  .titlebar svg { display: block; }
  .photo {
    height: calc(100% - 13px);
    background: radial-gradient(ellipse at 50% 45%, var(--photo-a), var(--photo-b));
  }
  .strip {
    position: absolute; top: 0; width: 10px; height: 190px;
    border: 1.5px solid var(--line);
  }
  .panel {
    position: absolute; top: 12px; height: 169px;
    border: 1.5px solid var(--line);
    display: flex; flex-direction: column; justify-content: center;
  }
  .quote { font-size: 13.6px; line-height: 16.8px; letter-spacing: 0.1px; }
  .author { font-style: italic; font-size: 13.6px; color: var(--author); margin-top: 3px; }

  .row.left .window { left: 0; }
  .row.left .strip { left: 204px; }
  .row.left .panel { left: 214px; right: 0; padding: 0 30px 0 15px; }

  .row.right .window { right: 0; }
  .row.right .strip { right: 204px; }
  .row.right .panel { left: 0; right: 214px; padding: 0 15px 0 15px; text-align: right; }
  .row.right .quote { text-align: justify; text-align-last: right; }

  .pink { background: var(--pink); }
  .purple { background: var(--purple); }
  .gray { background: var(--gray); }
  .blue { background: var(--blue); }
  .green { background: var(--green); }
  .yellow { background: var(--yellow); }
</style>
</head>
<body>
  <svg width="0" height="0" style="position:absolute">
    <defs>
      <g id="ctrl-min"><line x1="1" y1="4" x2="6" y2="4" stroke="#111" stroke-width="1"/></g>
      <g id="ctrl-max"><rect x="1" y="1" width="5" height="5" fill="none" stroke="#111" stroke-width="1"/></g>
      <g id="ctrl-add"><line x1="1" y1="3.5" x2="6" y2="3.5" stroke="#111" stroke-width="1"/><line x1="3.5" y1="1" x2="3.5" y2="6" stroke="#111" stroke-width="1"/></g>
    </defs>
  </svg>

  <section class="row left" style="top:33px">
    <div class="window">
      <div class="titlebar"><svg width="7" height="7"><use href="#ctrl-min"/></svg><svg width="7" height="7"><use href="#ctrl-max"/></svg><svg width="7" height="7"><use href="#ctrl-add"/></svg></div>
      <div class="photo" role="img" aria-label="Black and white portrait of Harold Wexbury"></div>
    </div>
    <div class="strip pink"></div>
    <div class="panel pink">
      <p class="quote">“What the pupil must learn, if he learns anything at all, is that the world will do most of the work for you, provided you cooperate with it by identifying how it really works and aligning with those realities. If we do not let the world teach us, it teaches us a lesson.”</p>
      <p class="author">Harold Wexbury</p>
    </div>
  </section>

  <section class="row right" style="top:226px">
    <div class="panel purple">
      <p class="quote">“I tackle every big new problem by asking two questions: Who has dealt with this problem well? And what can we learn from them?”</p>
      <p class="author">Tom Harlow</p>
    </div>
    <div class="strip purple"></div>
    <div class="window">
      <div class="titlebar"><svg width="7" height="7"><use href="#ctrl-min"/></svg><svg width="7" height="7"><use href="#ctrl-max"/></svg><svg width="7" height="7"><use href="#ctrl-add"/></svg></div>
      <div class="photo" role="img" aria-label="Black and white portrait of Tom Harlow"></div>
    </div>
  </section>

  <section class="row left" style="top:419px">
    <div class="window">
      <div class="titlebar"><svg width="7" height="7"><use href="#ctrl-min"/></svg><svg width="7" height="7"><use href="#ctrl-max"/></svg><svg width="7" height="7"><use href="#ctrl-add"/></svg></div>
      <div class="photo" role="img" aria-label="Black and white portrait of Ravindra Pallathuri"></div>
    </div>
    <div class="strip gray"></div>
    <div class="panel gray">
      <p class="quote">“If we can really understand the problem, the answer will come out of it, because the answer is not separate from the problem.”</p>
      <p class="author">Ravindra Pallathuri</p>
    </div>
  </section>

  <section class="row right" style="top:612px">
    <div class="panel blue">
      <p class="quote">“Success is nothing more than a few simple disciplines, practiced every day; while failure is simply a few errors in judgment, repeated every day. It is the accumulative weight of our disciplines and our judgments that leads us to either fortune or failure.”</p>
      <p class="author">Ned Pilsk</p>
    </div>
    <div class="strip blue"></div>
    <div class="window">
      <div class="titlebar"><svg width="7" height="7"><use href="#ctrl-min"/></svg><svg width="7" height="7"><use href="#ctrl-max"/></svg><svg width="7" height="7"><use href="#ctrl-add"/></svg></div>
      <div class="photo" role="img" aria-label="Black and white portrait of Ned Pilsk"></div>
    </div>
  </section>

  <section class="row left" style="top:805px">
    <div class="window">
      <div class="titlebar"><svg width="7" height="7"><use href="#ctrl-min"/></svg><svg width="7" height="7"><use href="#ctrl-max"/></svg><svg width="7" height="7"><use href="#ctrl-add"/></svg></div>
      <div class="photo" role="img" aria-label="Black and white portrait of Walt Brimsley"></div>
    </div>
    <div class="strip green"></div>
    <div class="panel green">
      <p class="quote" style="text-align:justify">“Inaction breeds doubt and fear. Action breeds confidence and courage.”</p>
      <p class="author">Walt Brimsley</p>
    </div>
  </section>

  <section class="row right" style="top:998px">
    <div class="panel yellow">
      <p class="quote">“What’s the one thing you can do, such that by doing it, everything else will be easier or unnecessary?”</p>
      <p class="author">Lenny Druse</p>
    </div>
    <div class="strip yellow"></div>
    <div class="window">
      <div class="titlebar"><svg width="7" height="7"><use href="#ctrl-min"/></svg><svg width="7" height="7"><use href="#ctrl-max"/></svg><svg width="7" height="7"><use href="#ctrl-add"/></svg></div>
      <div class="photo" role="img" aria-label="Black and white portrait of Lenny Druse"></div>
    </div>
  </section>
</body>
</html>
```